Tri Fold Brochure for Brookline Financial Planning SA

We need a tri fold and PDF (emailable) brochure for financial planning business located in a rural location in South Australia. I have attached the information we would like included. I would like the brochure to have a blue theme, as this is our corporate colour. I'm looking for something corporate, but not boring. It needs to catch the eye and engage our prospective clients. We have had some structural changes in the business and would like to portray a new company image that means business but is fresh and vibrant, yet very professional. It is possible that we could use the successful bid as a basis for our new website and further stationery needs.

Target Market(s)

Potential financial planning clients. We have a broad market 18-35 wealth accumulators, 35-50 wealth builders, 50-60 Pre-retirement, 60-75 retirement, 75+ Aged Care.

Industry/Entity Type

Financial Planning

Font styles to use
Sans Serif
Other font styles liked:
• Arial, verdana

Colors
0255a3
3176b5
85acd3
cfdeed
eaf1f7
ffffff
33a6d7
0392cd
85cae6

Requirements
Must have
• The Valmonte logo (which is in the uploaded material and cannot be changed), this needs to be placed close to the words as shown in the uploaded material. Our business logo. All the written information that I have attached less any design attributes I have attached. Some relatable photgraphs or images.
Nice to have
• The words "Certainty, Direction, and Peace of Mind" maybe in the back ground somewhere, sort of like a water mark. Any blue scheme is fine, with black and white included, take note of the version of blue in our logo. The fonts I have chosen can be used singularly or in a mixed format.
Should not have
• Photographs or designs used by other financial planning firms. Red, this is too confrontational.

```html
<!DOCTYPE html>
<html lang="en">
<head>
<meta charset="utf-8">
<title>Brookline Financial Planning SA – Tri-fold Brochure</title>
<link href="https://fonts.googleapis.com/css2?family=Roboto+Condensed:wght@700&family=Lato:wght@400&family=Roboto:wght@300;400&display=swap" rel="stylesheet">
<style>
  :root {
    --brand-blue: #2f3a96;
    --brand-navy: #2b3585;
    --charcoal: #3a3a3a;
    --ink: #333333;
    --white: #ffffff;
    --page: #e4e4e4;
    --paper: #ffffff;
  }
  * { margin: 0; padding: 0; box-sizing: border-box; }
  html, body { width: 1200px; height: 1200px; overflow: hidden; }
  body { background: var(--page); position: relative; font-family: "Lato", Arial, sans-serif; }

  .brochure {
    position: absolute; left: 81px; top: 233px;
    width: 1038px; height: 734px;
    background: var(--paper);
    overflow: hidden;
  }
  .brochure-art { position: absolute; inset: 0; width: 1038px; height: 734px; }

  .heading {
    position: absolute;
    font-family: "Roboto Condensed", Arial, sans-serif;
    font-weight: 700; text-transform: uppercase; line-height: 1;
  }
  .copy { position: absolute; font-size: 12px; line-height: 14.5px; }

  /* Panel: what we do */
  .what-we-do { left: 20px; top: 37px; font-size: 24px; color: var(--white); }
  .approach { left: 20px; top: 73px; width: 300px; color: var(--white); }
  .service-title {
    position: absolute; left: 20px; top: 134px;
    font-family: "Roboto Condensed", Arial, sans-serif; font-weight: 700;
    font-size: 16px; color: var(--white);
  }
  .service-list { position: absolute; left: 20px; top: 0; width: 320px; list-style: none; color: var(--white); }
  .service-list li, .help-list li {
    position: absolute; left: 0; font-size: 12px; line-height: 14.5px; padding-left: 13px; white-space: nowrap;
  }
  .service-list li::before, .help-list li::before {
    content: ""; position: absolute; left: 0; top: 4.5px;
    width: 6px; height: 6px; border-radius: 50%;
  }
  .service-list li::before { background: var(--white); }

  .help-title { left: 20px; top: 463px; font-size: 24px; color: var(--brand-blue); }
  .help-list { position: absolute; left: 20px; top: 0; list-style: none; color: var(--ink); }
  .help-list li::before { background: var(--brand-blue); }

  /* Panel: contact */
  .contact { position: absolute; left: 359px; width: 320px; text-align: center; color: var(--white); }
  .contact-title { left: 359px; width: 320px; top: 192px; font-size: 24px; text-align: center; color: var(--white); }
  .contact-line { position: absolute; left: 0; width: 100%; font-family: "Roboto", Arial, sans-serif; font-weight: 300; font-size: 13px; }
  .contact-icon { position: absolute; left: 150px; width: 20px; height: 20px; }
  .address {
    position: absolute; left: 359px; width: 320px; top: 653px;
    text-align: center; font-family: "Roboto", Arial, sans-serif; font-weight: 300;
    font-size: 13px; line-height: 17px; color: var(--ink);
  }

  /* Panel: cover */
  .brand-name {
    position: absolute; left: 750px; top: 29px;
    font-family: "Roboto", Arial, sans-serif; font-weight: 300;
    font-size: 24px; line-height: 25px; color: var(--brand-navy);
  }
  .tagline {
    position: absolute; right: 17px; top: 572px; text-align: right;
    font-family: "Roboto", Arial, sans-serif; font-weight: 300; color: var(--ink);
    text-transform: uppercase;
  }
  .tagline-line { display: block; font-size: 19px; line-height: 28px; }
  .tagline strong {
    font-family: "Roboto Condensed", Arial, sans-serif; font-weight: 700;
    color: var(--brand-blue); font-size: 26px;
  }
  .tagline .tagline-last { line-height: 34px; }
  .tagline .tagline-last strong { font-size: 31px; }
</style>
</head>
<body>
<main class="brochure">
  <svg class="brochure-art" viewBox="0 0 1298 917" xmlns="http://www.w3.org/2000/svg">
    <defs>
      <linearGradient id="deskTone" x1="0" y1="0" x2="1" y2="1">
        <stop offset="0" stop-color="#f4f4f6"/>
        <stop offset="1" stop-color="#dcdde2"/>
      </linearGradient>
      <linearGradient id="meetingTone" x1="0" y1="0" x2="1" y2="1">
        <stop offset="0" stop-color="#e6edf7"/>
        <stop offset="0.5" stop-color="#7f95b8"/>
        <stop offset="1" stop-color="#2c3f75"/>
      </linearGradient>
      <radialGradient id="chartTone" cx="0.6" cy="0.4" r="0.7">
        <stop offset="0" stop-color="#f3f8fd"/>
        <stop offset="0.6" stop-color="#9cc8ec"/>
        <stop offset="1" stop-color="#2a7fd0"/>
      </radialGradient>
    </defs>
    <!-- desk photo area, middle panel top -->
    <polygon points="431,0 864,0 864,236 431,58" fill="url(#deskTone)" role="img" aria-label="Photo of a calculator on a desk"/>
    <!-- main blue field -->
    <polygon class="blue-field" points="0,0 290,0 864,236 864,744 0,394" fill="#2f3a96"/>
    <polygon points="290,0 431,0 431,58" fill="#3a3a3a"/>
    <polygon points="0,394 174,469 0,564" fill="#3a3a3a"/>
    <!-- cover photo -->
    <polygon points="864,236 1298,68 1298,579 864,744" fill="url(#meetingTone)" role="img" aria-label="Photo of two business advisers reviewing a tablet"/>
    <polygon points="914,724 1298,575 1298,590 914,739" fill="#2f3a96"/>
    <polygon points="914,739 1298,590 1298,599 914,751" fill="#3a3a3a"/>
    <!-- round chart photo -->
    <circle cx="649" cy="646" r="136" fill="url(#chartTone)" stroke="#3a3a3a" stroke-width="8" role="img" aria-label="Photo of a hand marking pie chart reports with a pencil"/>
  </svg>

  <!-- Inside panel: what we do -->
  <h2 class="heading what-we-do">What we do</h2>
  <p class="copy approach">Our Approach is to simplify your financial situation, to make it understandable and manageable over the long term.</p>
  <h3 class="service-title">Our Service to You</h3>
  <ul class="service-list">
    <li style="top:159px">Different service packages tailored to your needs</li>
    <li style="top:188px">Options to have fees withdrawn from your investments</li>
    <li style="top:218px">We not only set goals, we monitor and review your<br>investments</li>
    <li style="top:263px">Hourly rate work offered</li>
  </ul>

  <h2 class="heading help-title">We can help you</h2>
  <ul class="help-list">
    <li style="top:496px">Save and accumulate wealth</li>
    <li style="top:526px">Protect your wealth</li>
    <li style="top:555px">Protect your family’s wealth</li>
    <li style="top:585px">Transition from work to retirement</li>
    <li style="top:615px">Maximise your retirement income</li>
    <li style="top:644px">With complex Centrelink situations and pension claims</li>
    <li style="top:674px">Manage the cost of Aged Care</li>
  </ul>

  <!-- Middle panel: contact -->
  <h2 class="heading contact-title">Contact us</h2>
  <div class="contact" style="top:0">
    <svg class="contact-icon" style="top:232px" viewBox="0 0 24 24" aria-hidden="true">
      <path d="M6.6 3.5l3 3.2-1.8 2.1c1 2.2 3 4.2 5.3 5.3l2.1-1.8 3.2 3-2 2.4c-5.7-.6-11.4-6.3-12-12z" fill="#ffffff"/>
    </svg>
    <span class="contact-line" style="top:259px">08 8000 4127</span>
    <svg class="contact-icon" style="top:291px" viewBox="0 0 24 24" aria-hidden="true">
      <path d="M3 10l9-7 9 7v11H3z M3 10l9 6 9-6 M3 21l7-6 M21 21l-7-6" fill="none" stroke="#ffffff" stroke-width="1.4" stroke-linejoin="round"/>
    </svg>
    <span class="contact-line" style="top:320px">office@brooklinefpsa.com.au</span>
    <svg class="contact-icon" style="top:345px" viewBox="0 0 24 24" aria-hidden="true">
      <g fill="none" stroke="#ffffff" stroke-width="1.3">
        <circle cx="12" cy="12" r="9"/><ellipse cx="12" cy="12" rx="4" ry="9"/>
        <path d="M3 12h18 M4.5 7.5h15 M4.5 16.5h15"/>
      </g>
    </svg>
    <span class="contact-line" style="top:366px">www.brooklinefpsa.com.au</span>
  </div>
  <address class="address" style="font-style:normal">
    Brookline Financial Planning SA<br>
    Level 1 14 Riverbend Road<br>
    MILLBROOK&nbsp; SA&nbsp; 5399
  </address>

  <!-- Cover panel -->
  <p class="brand-name">Brookline<br>Financial<br>Planning SA</p>
  <h1 class="tagline">
    <span class="tagline-line"><strong>We partner</strong></span>
    <span class="tagline-line">with our&nbsp; <strong>clients</strong></span>
    <span class="tagline-line">to create a <strong>roadmap</strong> for</span>
    <span class="tagline-line tagline-last">their <strong>financial future</strong></span>
  </h1>
</main>
</body>
</html>
```